valtheon construction

i want a construction website something that really epic and eye catchy

we do full Renovation Restoration Construction

if anyone can make my jaw drop there well be a big Reward ,

i have attach my logo

Industry/Entity Type

Construction

Number of Pages Required

4 page

```html
<!DOCTYPE html>
<html lang="en">
<head>
<meta charset="utf-8">
<title>Valtheon Construction Co.</title>
<link href="https://fonts.googleapis.com/css2?family=Roboto:wght@300;400;500;700&family=Open+Sans:wght@400;600&display=swap" rel="stylesheet">
<style>
:root{
  --red:#b3121b;
  --red-dark:#8e0b12;
  --ink:#222;
  --muted:#666;
  --light:#f4f4f4;
  --footer:#2b2b2b;
  --footer-bar:#1c1c1c;
  --footer-text:#aaa;
  --white:#fff;
}
*{box-sizing:border-box;margin:0;padding:0}
html,body{width:870px;height:1200px;overflow:hidden;background:var(--white)}
body{font-family:"Open Sans",sans-serif;color:var(--ink)}
.page{width:870px;height:1200px;position:relative}

.site-header{height:100px;display:flex;align-items:center;justify-content:space-between;padding:0 60px 0 58px;background:var(--white)}
.brand{display:flex;align-items:center;gap:10px}
.brand-mark{width:30px;height:30px;background:var(--red)}
.brand-name{font-family:"Roboto",sans-serif;font-weight:700;color:var(--red);font-size:19px;line-height:1.05;letter-spacing:.5px;text-transform:uppercase}
.main-nav{display:flex;gap:6px}
.main-nav a{font-family:"Roboto",sans-serif;font-size:12px;color:#444;text-decoration:none;padding:8px 13px;border:1px solid transparent}
.main-nav a.active{border-color:var(--red);color:var(--red)}

.hero{position:relative;height:305px}
.hero-photo{position:absolute;inset:0;background:linear-gradient(100deg,#f1f1f0 0%,#e4e4e2 45%,#d2d3d0 75%,#b9bbb6 100%)}
.hero-content{position:relative;padding:52px 0 0 88px}
.hero-title{font-family:"Roboto",sans-serif;font-weight:500;font-size:34px;line-height:1.25;color:var(--red-dark)}
.hero-btn{display:inline-block;margin-top:26px;background:var(--red);color:var(--white);font-family:"Roboto",sans-serif;font-size:12px;font-weight:500;padding:11px 18px;letter-spacing:.5px}

.contact-band{height:175px;background:var(--red);text-align:center;padding-top:32px}
.contact-band h2{font-family:"Roboto",sans-serif;font-weight:300;color:var(--white);font-size:32px}
.subscribe-form{display:flex;justify-content:center;gap:8px;margin-top:22px}
.subscribe-form .field{width:170px;height:30px;border:1px solid rgba(255,255,255,.45);background:rgba(0,0,0,.08);color:#f3d4d6;font-size:11px;text-align:left;padding:8px 10px}
.subscribe-form .btn{height:30px;border:1px solid var(--white);color:var(--white);font-family:"Roboto",sans-serif;font-size:14px;padding:5px 14px}

.welcome{text-align:center;padding-top:22px}
.welcome h2{font-family:"Roboto",sans-serif;font-weight:400;font-size:34px;color:var(--ink)}
.welcome p{width:500px;margin:10px auto 0;font-size:11px;line-height:1.6;color:var(--muted)}

.services{display:flex;gap:20px;justify-content:center;margin-top:26px}
.service{width:220px}
.service-photo{height:122px}
.service h3{font-family:"Roboto",sans-serif;font-weight:400;font-size:26px;color:var(--red);margin-top:14px}
.service p{font-size:11px;line-height:1.6;color:var(--muted);margin-top:4px}
.p-renovation{background:linear-gradient(135deg,#d9dde2,#c2c7cd 60%,#b4222a)}
.p-restoration{background:linear-gradient(135deg,#7c8fa6,#6b6f75 55%,#8a6a4a)}
.p-construction{background:linear-gradient(160deg,#6fa3d6,#a9c8e6 50%,#c9a14d)}

.site-footer{position:absolute;left:0;right:0;top:985px;height:185px;background:var(--footer);display:grid;grid-template-columns:130px 190px 220px 200px;gap:0;padding:20px 0 0 58px;color:var(--footer-text);font-size:9px;line-height:1.5}
.site-footer h4{font-family:"Roboto",sans-serif;font-weight:500;color:var(--white);font-size:11px;margin-bottom:12px}
.link-list li{list-style:none;margin-bottom:2px}
.feed-item{display:flex;gap:8px;margin-bottom:10px}
.feed-thumb{width:26px;height:26px;background:#555;flex:none}
.tweet-dot{width:16px;height:16px;border-radius:50%;background:#555;flex:none}
.feed-item b{color:#ddd;font-weight:600}
.social-row{display:flex;align-items:center;gap:6px;margin-bottom:6px}
.social-row svg{flex:none}
.social-icons{display:flex;gap:6px;margin-top:6px}
.social-icons span{width:14px;height:14px;border-radius:50%;background:#555}
.footer-bar{position:absolute;left:0;right:0;bottom:0;height:30px;background:var(--footer-bar);color:var(--footer-text);font-size:9px;text-align:center;line-height:30px}
.footer-bar strong{color:var(--red);font-weight:400}
</style>
</head>
<body>
<div class="page">
  <header class="site-header">
    <div class="brand">
      <span class="brand-mark"></span>
      <span class="brand-name">Valtheon<br>Construction Co.</span>
    </div>
    <nav class="main-nav">
      <a class="active" href="#">HOME</a>
      <a href="#">ABOUT</a>
      <a href="#">MANAGEMENT</a>
      <a href="#">PROJECT</a>
      <a href="#">CLIENT</a>
      <a href="#">CONTACT</a>
    </nav>
  </header>

  <section class="hero">
    <div class="hero-photo" role="img" aria-label="Bright white modern living room interior with sofa and plants"></div>
    <div class="hero-content">
      <h1 class="hero-title">We are a Creative<br>Renovation &amp; Restortion Design Studio</h1>
      <span class="hero-btn">GET STARTED</span>
    </div>
  </section>

  <section class="contact-band">
    <h2>Interested Get in Touch With Us</h2>
    <div class="subscribe-form">
      <span class="field">Name</span>
      <span class="field">Company Name</span>
      <span class="field">E-Mail</span>
      <span class="btn">Subscribe</span>
    </div>
  </section>

  <section class="welcome">
    <h2>Welcome to VALTHEON CONSTRUCTION CO.</h2>
    <p>Lorem Ipsum is simply dummy text of the printing and typesetting industry. Lorem Ipsum has been the industry's standard dummy text ever since the 1500s, when an unknown printer took a galley of type and scrambled it to make a type specimen book.</p>
  </section>

  <section class="services">
    <article class="service">
      <div class="service-photo p-renovation" role="img" aria-label="Worker in red overalls renovating a wall"></div>
      <h3>Renovation</h3>
      <p>Lorem Ipsum is simply dummy text of the printing and typesetting industry. Lorem Ipsum has been the industry.</p>
    </article>
    <article class="service">
      <div class="service-photo p-restoration" role="img" aria-label="Workers restoring a building structure"></div>
      <h3>Restoration</h3>
      <p>Lorem Ipsum is simply dummy text of the printing and typesetting industry. Lorem Ipsum has been the industry.</p>
    </article>
    <article class="service">
      <div class="service-photo p-construction" role="img" aria-label="Building under construction with cranes against blue sky"></div>
      <h3>Construction</h3>
      <p>Lorem Ipsum is simply dummy text of the printing and typesetting industry. Lorem Ipsum has been the industry.</p>
    </article>
  </section>

  <footer class="site-footer">
    <div>
      <h4>Links</h4>
      <ul class="link-list">
        <li>Home</li><li>Privacy Policy</li><li>Terms &amp; Conditions</li><li>FAQ's</li>
      </ul>
    </div>
    <div>
      <h4>NEWS FEED</h4>
      <div class="feed-item"><span class="feed-thumb"></span><div><b>Lena Hart</b> posted a new blog<br>Today 2:30 pm · 12/06/2015</div></div>
      <div class="feed-item"><span class="feed-thumb"></span><div><b>Owen Brooks</b> posted a message on Renovation<br>Today 1:15 pm · 12/06/2015</div></div>
    </div>
    <div>
      <h4>RECENT TWEETS</h4>
      <div class="feed-item"><span class="tweet-dot"></span><div>@designquote @VALTHEON<br>Thank you very much!<br>4 days ago</div></div>
      <div class="feed-item"><span class="tweet-dot"></span><div>@teamquote @VALTHEON<br>Thank you very much!<br>4 days ago</div></div>
    </div>
    <div>
      <h4>Social Links</h4>
      <div class="social-row"><svg width="10" height="12" viewBox="0 0 10 12"><path d="M5 0a4 4 0 0 1 4 4c0 3-4 8-4 8S1 7 1 4a4 4 0 0 1 4-4z" fill="#aaa"/><circle cx="5" cy="4" r="1.5" fill="#2b2b2b"/></svg><span>Lorem Ipsum is simply dummy text of the print</span></div>
      <div class="social-row"><svg width="10" height="10" viewBox="0 0 10 10"><path d="M2 0l2 2-1 1.5a6 6 0 0 0 3.5 3.5L8 6l2 2-1.5 2C4 10 0 6 0 1.5z" fill="#aaa"/></svg><span>123 456 7890</span></div>
      <div class="social-row"><svg width="11" height="8" viewBox="0 0 11 8"><rect width="11" height="8" fill="#aaa"/><path d="M0 0l5.5 4.5L11 0" stroke="#2b2b2b" fill="none"/></svg><span>info@valtheon.com</span></div>
      <div class="social-icons"><span></span><span></span><span></span><span></span><span></span><span></span></div>
    </div>
  </footer>
  <div class="footer-bar">© <strong>VALTHEON</strong> - 2015. All Rights Reserved.</div>
</div>
</body>
</html>
```